Graphics Design of Physics Book

Hi
Size : 8" x 11.25"
We are education book Publication Company and would like to have book cover for "Physics" it has 4 volumes. All 4 having the same color scheme and design except the volume no.
Blue is my personal favorite but u can use any color. Want to have a band at the bottom of the cover to place our Logo “VORLIN Education” a PDF of the same is attached, or you can place logo anywhere according to ur design.
I need “Physics” as title of the book to be visible prominently.
And volume and volume no. should also be Visible and eye catching I prefer a Graphic to enhance the Volume No.
A background pattern can also be a option (it should be vector form so that color can be change later)
Please do not offer any cut and paste design I need very professional presentation.
Volume and Number can be in metallic 3D (CMYK) effect.
only Professional presentation will get feedback.
I have provided a sample artwork for reference do not follow it but can be a reference what I needed !

Target Market(s)

Students Class 9th to 12th

Industry/Entity Type

Education

Font styles to use
Serif

Colors
3176b5
0555a3
85abd2
cadf82
abd036
9bcb3c

Requirements
Must have
• Eye catching.
• “Physics” as title of the book to be visible prominently.
• volume and volume no. should also be Visible and eye catching
• I prefer a Graphic to enhance the Volume No.
• Icons for
• 1. Questions and answers
• 2. Theory Notes
• 3. Tips & Tricks
• 4. Previous Year's Reference Questions
• 5. Covers Complete Syllabus
Nice to have
• decent seamless background or metallic 3d effect (not to be print in special Ink) design should only be in CMYK.
Should not have
• Physics related Pictures or Icons (Specially E=mc2) or any scientist photograph or I Need pure graphic design

```html
<!DOCTYPE html>
<html lang="en">
<head>
<meta charset="UTF-8">
<title>Physics Volume 4 – Book Cover</title>
<link rel="stylesheet" href="https://fonts.googleapis.com/css2?family=Playfair+Display:wght@700;900&display=swap">
<style>
  :root {
    --page-bg: #cfc7c2;
    --cover-deep: #0b2a66;
    --cover-mid: #0555a3;
    --cover-light: #3176b5;
    --cover-glow: #4e94cf;
    --title-white: #f4f6f8;
    --title-shadow: #041636;
    --silver-light: #f2f3f5;
    --silver-mid: #c9ccd1;
    --silver-dark: #8e939b;
    --volume-blue: #0f5aa8;
    --icon-line: #e8eef6;
    --icon-fill: #0a4f9a;
  }
  * { margin: 0; padding: 0; box-sizing: border-box; }
  html, body {
    width: 1200px;
    height: 1000px;
    overflow: hidden;
    background: var(--page-bg);
  }
  .book-cover {
    position: absolute;
    left: 280px;
    top: 50px;
    width: 640px;
    height: 900px;
    overflow: hidden;
    background:
      radial-gradient(ellipse 70% 45% at 50% 48%, var(--cover-glow) 0%, var(--cover-light) 35%, transparent 75%),
      linear-gradient(180deg, var(--cover-deep) 0%, var(--cover-mid) 45%, var(--cover-mid) 60%, var(--cover-deep) 100%);
    box-shadow: 0 10px 30px rgba(0,0,0,0.25);
  }
  .cover-pattern {
    position: absolute;
    inset: 0;
    background: radial-gradient(ellipse at 50% 50%, rgba(255,255,255,0.06), rgba(0,0,0,0.08));
  }
  .cover-title {
    position: absolute;
    top: 60px;
    left: 0;
    width: 100%;
    text-align: center;
    font-family: "Playfair Display", serif;
    font-weight: 900;
    font-size: 104px;
    line-height: 1;
    color: var(--title-white);
    text-shadow: 4px 5px 0 var(--title-shadow);
  }
  .volume-badge {
    position: absolute;
    left: 137px;
    top: 225px;
    width: 366px;
    height: 320px;
  }
  .volume-badge svg { position: absolute; inset: 0; }
  .volume-label {
    position: absolute;
    top: 30px;
    width: 100%;
    text-align: center;
    font-family: "Playfair Display", serif;
    font-weight: 900;
    font-size: 26px;
    letter-spacing: 1px;
    color: var(--volume-blue);
  }
  .volume-number {
    position: absolute;
    top: 40px;
    width: 100%;
    text-align: center;
    font-family: "Playfair Display", serif;
    font-weight: 900;
    font-size: 250px;
    line-height: 1;
    color: var(--silver-light);
    background: linear-gradient(100deg, #ffffff 0%, #d9dce0 35%, #9aa0a8 55%, #eef0f2 75%, #b9bdc3 100%);
    -webkit-background-clip: text;
    background-clip: text;
    -webkit-text-fill-color: transparent;
    filter: drop-shadow(6px 6px 0 #7d828a) drop-shadow(3px 3px 3px rgba(0,0,0,0.35));
  }
  .feature-icons {
    position: absolute;
    top: 608px;
    left: 0;
    width: 100%;
    display: flex;
    justify-content: center;
    gap: 8px;
  }
  .feature-icon { width: 72px; height: 66px; }
  .publisher-name {
    position: absolute;
    top: 765px;
    left: 0;
    width: 100%;
    text-align: center;
    font-family: "Playfair Display", serif;
    font-weight: 700;
    font-size: 40px;
    color: var(--title-white);
  }
</style>
</head>
<body>
  <main class="book-cover">
    <div class="cover-pattern" role="img" aria-label="Subtle diamond and fine horizontal stripe background pattern"></div>

    <h1 class="cover-title">PHYSICS</h1>

    <div class="volume-badge">
      <svg viewBox="0 0 366 320" width="366" height="320">
        <defs>
          <linearGradient id="silverFrame" x1="0" y1="0" x2="1" y2="1">
            <stop offset="0" stop-color="#ffffff"/>
            <stop offset="0.5" stop-color="#9aa0a8"/>
            <stop offset="1" stop-color="#e6e8eb"/>
          </linearGradient>
          <linearGradient id="silverFace" x1="0" y1="0" x2="1" y2="1">
            <stop offset="0" stop-color="#e9ebee"/>
            <stop offset="1" stop-color="#c4c8cd"/>
          </linearGradient>
        </defs>
        <polygon points="0,160 91,0 275,0 366,160 275,320 91,320" fill="url(#silverFrame)"/>
        <polygon points="12,160 98,12 268,12 354,160 268,308 98,308" fill="url(#silverFace)"/>
      </svg>
      <div class="volume-label">VOLUME</div>
      <div class="volume-number">4</div>
    </div>

    <div class="feature-icons">
      <svg class="feature-icon" viewBox="0 0 72 66" aria-label="Questions and answers">
        <polygon points="2,33 19,2 53,2 70,33 53,64 19,64" fill="var(--icon-fill)" stroke="var(--icon-line)" stroke-width="2.5"/>
        <text x="36" y="40" text-anchor="middle" font-family="Playfair Display, serif" font-weight="900" font-size="20" fill="var(--icon-line)">QA</text>
      </svg>
      <svg class="feature-icon" viewBox="0 0 72 66" aria-label="Theory notes">
        <polygon points="2,33 19,2 53,2 70,33 53,64 19,64" fill="var(--icon-fill)" stroke="var(--icon-line)" stroke-width="2.5"/>
        <rect x="24" y="18" width="22" height="30" fill="none" stroke="var(--icon-line)" stroke-width="2"/>
        <line x1="28" y1="25" x2="42" y2="25" stroke="var(--icon-line)" stroke-width="2"/>
        <line x1="28" y1="31" x2="42" y2="31" stroke="var(--icon-line)" stroke-width="2"/>
        <line x1="28" y1="37" x2="38" y2="37" stroke="var(--icon-line)" stroke-width="2"/>
        <line x1="40" y1="46" x2="50" y2="30" stroke="var(--icon-line)" stroke-width="3"/>
      </svg>
      <svg class="feature-icon" viewBox="0 0 72 66" aria-label="Tips and tricks">
        <polygon points="2,33 19,2 53,2 70,33 53,64 19,64" fill="var(--icon-fill)" stroke="var(--icon-line)" stroke-width="2.5"/>
        <circle cx="36" cy="30" r="9" fill="none" stroke="var(--icon-line)" stroke-width="2"/>
        <rect x="32" y="39" width="8" height="6" fill="var(--icon-line)"/>
        <line x1="36" y1="14" x2="36" y2="17" stroke="var(--icon-line)" stroke-width="2"/>
        <line x1="22" y1="30" x2="25" y2="30" stroke="var(--icon-line)" stroke-width="2"/>
        <line x1="47" y1="30" x2="50" y2="30" stroke="var(--icon-line)" stroke-width="2"/>
        <line x1="26" y1="20" x2="28" y2="22" stroke="var(--icon-line)" stroke-width="2"/>
        <line x1="46" y1="20" x2="44" y2="22" stroke="var(--icon-line)" stroke-width="2"/>
      </svg>
      <svg class="feature-icon" viewBox="0 0 72 66" aria-label="Previous year's reference questions">
        <polygon points="2,33 19,2 53,2 70,33 53,64 19,64" fill="var(--icon-fill)" stroke="var(--icon-line)" stroke-width="2.5"/>
        <rect x="23" y="38" width="26" height="7" fill="none" stroke="var(--icon-line)" stroke-width="2"/>
        <rect x="25" y="29" width="24" height="7" fill="none" stroke="var(--icon-line)" stroke-width="2"/>
        <rect x="23" y="20" width="26" height="7" fill="none" stroke="var(--icon-line)" stroke-width="2"/>
      </svg>
      <svg class="feature-icon" viewBox="0 0 72 66" aria-label="Covers complete syllabus">
        <polygon points="2,33 19,2 53,2 70,33 53,64 19,64" fill="var(--icon-fill)" stroke="var(--icon-line)" stroke-width="2.5"/>
        <rect x="24" y="17" width="24" height="32" fill="none" stroke="var(--icon-line)" stroke-width="2"/>
        <line x1="28" y1="23" x2="44" y2="23" stroke="var(--icon-line)" stroke-width="2"/>
        <polyline points="29,35 34,40 44,29" fill="none" stroke="var(--icon-line)" stroke-width="3"/>
      </svg>
    </div>

    <div class="publisher-name">VORLIN Education</div>
  </main>
</body>
</html>
```